Cortelune Pamphlet

We need to design a pamplet for Cortelune, a Bespoke Wine Cellar design and build company. Our logo and signature cellar should be incorperated into the design (can be seen at www.cortelune-example.com). It should also include what will be called the template with a scematic drawing of a cellar to outline the key features An area called the process will showcase the different types of materials that can be used and there neesa to be indicative costs dependant in size also somewhere, as well as the fact that design £950+VAT but will be taken off the cost of the cellar if we do the job refunded back into project on approval.
.
Updates

Industry/Entity Type

It Company

```html
<!DOCTYPE html>
<html lang="en">
<head>
<meta charset="utf-8">
<title>Cortelune Pamphlet</title>
<link href="https://fonts.googleapis.com/css2?family=Lato:wght@400;700&family=Josefin+Sans:wght@300&display=swap" rel="stylesheet">
<style>
  :root {
    --paper: #ffffff;
    --ink: #000000;
    --text: #ffffff;
    --cellar-blue-1: #2b3f9e;
    --cellar-blue-2: #6a8be0;
    --cellar-blue-3: #7a4a58;
    --white-rack-1: #f1f1f1;
    --white-rack-2: #b9b9b9;
    --dark-rack-1: #3a3330;
    --dark-rack-2: #0f0e0d;
    --hall-1: #3f4352;
    --hall-2: #b7875a;
    --glass-1: #1a2418;
    --glass-2: #5e5136;
    --glass-light: #8a8c58;
  }
  * { box-sizing: border-box; margin: 0; padding: 0; }
  html, body {
    width: 1200px;
    height: 856px;
    overflow: hidden;
    background: var(--paper);
  }
  .pamphlet {
    position: relative;
    width: 1200px;
    height: 856px;
    background: var(--paper);
  }
  .spread {
    position: absolute;
    left: 3px;
    top: 8px;
    width: 1193px;
    height: 845px;
    background: var(--ink);
  }
  .photo { position: absolute; }
  .photo--signature-cellar {
    left: 14px; top: 16px; width: 331px; height: 486px;
    background: radial-gradient(ellipse at 50% 35%, var(--cellar-blue-2), var(--cellar-blue-1) 60%, var(--cellar-blue-3));
  }
  .photo--template-rack {
    left: 361px; top: 16px; width: 212px; height: 232px;
    background: linear-gradient(180deg, var(--white-rack-1), var(--white-rack-2));
  }
  .photo--dark-rack {
    left: 361px; top: 268px; width: 212px; height: 234px;
    background: linear-gradient(180deg, var(--dark-rack-1), var(--dark-rack-2) 70%, #4b4742);
  }
  .photo--hallway {
    left: 614px; top: 16px; width: 200px; height: 486px;
    background: linear-gradient(180deg, var(--hall-1) 10%, #4a4b55 55%, var(--hall-2));
  }
  .photo--glass-top {
    left: 832px; top: 16px; width: 125px; height: 232px;
    background: linear-gradient(180deg, var(--glass-1), #2c3526);
  }
  .photo--glass-bottom {
    left: 832px; top: 268px; width: 125px; height: 234px;
    background: linear-gradient(180deg, #1c2119, var(--glass-2));
  }
  .photo--glass-room {
    left: 974px; top: 16px; width: 201px; height: 486px;
    background: linear-gradient(160deg, var(--glass-1) 20%, var(--glass-light) 55%, var(--glass-2));
  }
  .brand {
    position: absolute;
    left: 40px;
    top: 708px;
    width: 260px;
    text-align: center;
    font-family: "Josefin Sans", sans-serif;
    font-weight: 300;
    font-size: 27px;
    letter-spacing: 5px;
    color: var(--text);
  }
  .copy {
    position: absolute;
    color: var(--text);
    font-family: "Lato", sans-serif;
    font-size: 13.4px;
    text-align: justify;
    hyphens: auto;
  }
  .copy p + p { margin-top: 12px; }
  .copy--template {
    left: 361px; top: 580px; width: 212px;
    line-height: 12.2px;
    letter-spacing: -0.2px;
  }
  .copy--process {
    left: 648px; top: 580px; width: 246px;
    line-height: 14.4px;
  }
  .copy--costs {
    left: 925px; top: 580px; width: 248px;
    line-height: 14.4px;
  }
  .copy--process p + p, .copy--costs p + p { margin-top: 14px; }
</style>
</head>
<body>
<main class="pamphlet">
  <section class="spread">
    <div class="photo photo--signature-cellar" role="img" aria-label="Signature cellar: blue-lit gothic arch of bottle racks with three large stone spheres on a parquet floor"></div>
    <div class="photo photo--template-rack" role="img" aria-label="Schematic rendering of the template cellar with bottle racks and shelving"></div>
    <div class="photo photo--dark-rack" role="img" aria-label="Dark wood wine cellar with illuminated bottle shelves and crates"></div>
    <div class="photo photo--hallway" role="img" aria-label="Hallway with herringbone floor, dark wall and sunburst mirror leading to the cellar"></div>
    <div class="photo photo--glass-top" role="img" aria-label="Glass-walled cellar with bottles on wall-mounted racks"></div>
    <div class="photo photo--glass-bottom" role="img" aria-label="Glass cellar door over a herringbone wood floor"></div>
    <div class="photo photo--glass-room" role="img" aria-label="Glass wine room with lit bottle racks and a backlit onyx wall"></div>

    <div class="brand">CORTELUNE</div>

    <div class="copy copy--template">
      <p>The template is our schematic of a Cortelune cellar, outlining the key features of every build: insulated walls and ceiling, a vapour barrier, climate control, frameless glass doors, LED lighting, bespoke racking and a sealed floor, all planned around your home.</p>
      <p>Each template is drawn to your space, so you can see how your bottles will be stored, displayed and kept at the perfect temperature.</p>
    </div>

    <div class="copy copy--process">
      <p>The process begins with materials. Choose from oak, walnut or reclaimed timber racking, brushed steel rods and cable systems, acrylic pegs, natural stone, polished concrete or backlit onyx, framed or frameless glass and herringbone wood floors, each sampled by our craftsmen.</p>
      <p>We guide you from the first sketch to the final installation, so every material suits the room, the light and the wines it will hold.</p>
    </div>

    <div class="copy copy--costs">
      <p>Indicative costs depend on size. A cabinet or under-stair cellar of up to 300 bottles starts from £15,000. A walk-in room of up to 1,000 bottles starts from £35,000, and a signature cellar of 2,000 bottles or more from £75,000, all plus VAT.</p>
      <p>Design is £950 + VAT. If we build your cellar, the full fee is refunded back into the project on approval of the design.</p>
    </div>
  </section>
</main>
</body>
</html>
```